Book and Ebook Cover for my Upcoming Book

About the Book
------------------
I need a book, ebook and if possible audio cover design for my upcoming book - Lanterns & Larkspur. This is my first book and really looking for a great book cover. The book is about my story, living with Mental Health and how to reclaim control of your life.

Quillbarrow
-----------
I am using quillbarrow.com to self-publish my book so in case of any design-related questions you can just search info on their website.

I have an initial theme I am thinking for the design book cover which I have attached. You can use this as a starting point.

Idea for the theme
---------------------
I am thinking about a phoenix to represent rising from the ashes and rebirth. The phoenix motif will be continued throughout the interior pages of the book. I'd like the cover of the book to be minimal, white with gold lettering, and maybe incorporating wings? feel free to play around with the idea and up for suggestions.

If you can think of something along these lines and make it a lot better that would be great.

What I need
---------------
The book is complete and is Trim size is 6.14 x 9.21” (234 x 156mm). I would need-
1. Book Cover
2. Back & Spine Design
3. Source File
4. Ebook Cover
5. Need multiple revisions to get the best possible outcome
6. My name and book title should also on the front cover
7. The book title should be bigger size than the subtitle

If you can give me Audiobook cover, I would love that as well and can pay extra for it if needed.

I love this for the interior phoenix motif:
https://craftbazaarly.com/InkMoth/7720458-Watercolor-Heron-Clipart-Set#fullscreen

The only other actual book cover I found online that remotely relates to what I am looking for is this -
https://www.lookfinder.example/url?sa=i&url=https%3A%2F%2Fpixelmoor.com%2Fvantrell&psig=QxTrPLm3KZ9vBwE2dYcN41HoJuSA&ust=1598415525610000&source=images&cd=vfe&ved=0CAIQjRxqFwoTCPD_toPAtesCFQAAAAAdAAAAABAD

Target Market(s)

Personal Development
Mental health

Requirements
Must have
• 1. Book Cover
2. Back & Spine Design
3. Source File
4. Ebook Cover
Nice to have
• Audiobook cover as I eventually will be releasing the audio version of the book

```html
<!DOCTYPE html>
<html lang="en">
<head>
<meta charset="utf-8">
<title>Lanterns &amp; Larkspur — Cover Wrap</title>
<link href="https://fonts.googleapis.com/css2?family=Bebas+Neue&family=Montserrat:wght@400;500&display=swap" rel="stylesheet">
<style>
  :root {
    --ink-white: #ffffff;
    --ash-black: #151312;
    --placeholder: #ececec;
    --shadow: rgba(0, 0, 0, 0.75);
  }
  * { box-sizing: border-box; margin: 0; padding: 0; }
  html, body { width: 1200px; height: 864px; overflow: hidden; background: var(--ash-black); }

  .cover-wrap {
    position: relative;
    width: 1200px;
    height: 864px;
    overflow: hidden;
    color: var(--ink-white);
    font-family: "Montserrat", sans-serif;
  }

  .cover-art {
    position: absolute;
    inset: 0;
    background:
      radial-gradient(ellipse 150px 190px at 960px 260px, rgba(243,154,60,0.85), rgba(232,86,28,0.35) 55%, transparent 75%),
      radial-gradient(ellipse 90px 260px at 930px 520px, rgba(232,86,28,0.45), transparent 70%),
      radial-gradient(ellipse 260px 60px at 1120px 640px, rgba(232,86,28,0.55), transparent 70%),
      radial-gradient(ellipse 220px 50px at 760px 620px, rgba(232,86,28,0.4), transparent 70%),
      radial-gradient(ellipse 120px 220px at 210px 330px, rgba(232,86,28,0.55), transparent 70%),
      radial-gradient(ellipse 320px 70px at 140px 680px, rgba(232,86,28,0.45), transparent 70%),
      radial-gradient(ellipse 200px 60px at 500px 580px, rgba(232,86,28,0.35), transparent 70%),
      linear-gradient(180deg, #2a2726 0%, #3b3431 35%, #4a2f24 55%, #2b201c 75%, #1b1614 100%);
  }

  /* Back cover */
  .back-title {
    position: absolute;
    left: 120px;
    top: 56px;
    width: 346px;
    text-align: center;
    font-family: "Bebas Neue", sans-serif;
    font-weight: 400;
    text-shadow: 3px 3px 4px var(--shadow);
  }
  .back-title .title-word { display: block; font-size: 100px; line-height: 84px; }
  .back-title .title-amp { display: block; font-size: 24px; line-height: 34px; }

  .back-blurb {
    position: absolute;
    left: 61px;
    top: 271px;
    width: 456px;
    font-size: 11.2px;
    line-height: 15px;
    text-align: justify;
    text-shadow: 1px 1px 2px var(--shadow);
  }
  .back-blurb p { text-indent: 18px; margin-bottom: 3px; }

  .about-author {
    position: absolute;
    left: 61px;
    top: 658px;
    width: 456px;
    display: flex;
    gap: 11px;
  }
  .author-photo {
    flex: 0 0 95px;
    height: 118px;
    background: var(--placeholder);
  }
  .author-bio { font-size: 11.2px; line-height: 14.6px; text-align: justify; text-shadow: 1px 1px 2px var(--shadow); }
  .author-bio h3 { font-size: 11.5px; font-weight: 500; letter-spacing: 0.02em; }

  /* Spine */
  .spine-title, .spine-author {
    position: absolute;
    writing-mode: vertical-rl;
    font-family: "Bebas Neue", sans-serif;
    white-space: nowrap;
    text-shadow: 2px 2px 3px var(--shadow);
  }
  .spine-title { left: 579px; top: 124px; font-size: 36px; letter-spacing: 0.26em; line-height: 36px; }
  .spine-title .spine-amp { font-size: 18px; letter-spacing: 0.2em; }
  .spine-author { left: 588px; top: 655px; font-size: 23px; letter-spacing: 0.04em; line-height: 22px; }

  /* Front cover */
  .front-title {
    position: absolute;
    left: 680px;
    top: 252px;
    width: 520px;
    text-align: center;
    font-family: "Bebas Neue", sans-serif;
    font-weight: 400;
    text-shadow: 4px 4px 5px var(--shadow);
  }
  .front-title .title-word { display: block; font-size: 150px; line-height: 136px; }
  .front-title .title-amp { display: block; font-size: 44px; line-height: 50px; }

  .front-author {
    position: absolute;
    left: 680px;
    top: 744px;
    width: 520px;
    text-align: center;
    font-family: "Bebas Neue", sans-serif;
    font-size: 48px;
    letter-spacing: 0.04em;
    text-shadow: 3px 3px 4px var(--shadow);
  }
</style>
</head>
<body>
  <div class="cover-wrap">
    <div class="cover-art" role="img" aria-label="Dark volcanic landscape with glowing lava cracks and an erupting volcano, a fiery phoenix rising from the embers on the front cover"></div>

    <section class="back-cover">
      <h2 class="back-title">
        <span class="title-word">Lanterns</span>
        <span class="title-amp">&amp;</span>
        <span class="title-word">Larkspur</span>
      </h2>

      <div class="back-blurb">
        <p>Lorem ipsum dolor sit amet, consectetur adipiscing elit. Sed malesuada a ipsum a tincidunt. Etiam ut tortor quam. Morbi massa libero, rhoncus at efficitur eget, condimentum a nibh. Morbi ultrices venenatis sodales. Aenean dictum justo nec condimentum egestas. Etiam ligula nibh, vulputate quis enim in, pulvinar mattis enim. Vivamus vel imperdiet tellus. Maecenas pretium pretium odio sodales consequat. Donec metus lectus, ornare nec euismod quis, imperdiet in purus. Praesent sagittis viverra efficitur. Suspendisse fermentum sollicitudin diam, sed varius dui ullamcorper vel. Vivamus at eleifend nisi, vel rhoncus libero. Nullam molestie, leo eget tristique rhoncus, turpis leo viverra enim, vitae tincidunt lectus orci vel odio. Vestibulum id nulla accumsan, porta leo vitae, vulputate dui. Cras tempor tempor nisl.</p>
        <p>Nam tincidunt cursus diam et imperdiet. Vestibulum dignissim enim eu venenatis luctus. Nullam dignissim volutpat laoreet. Quisque vehicula eleifend hendrerit. Cras commodo facilisis mauris. Etiam eget libero blandit, scelerisque velit id, fermentum odio. Quisque pharetra porttitor sapien id aliquet. Proin sodales rhoncus elit, non gravida sem sodales quis. Duis hendrerit suscipit enim.</p>
        <p>Nam eu bibendum augue. Morbi malesuada, lectus a consequat faucibus, sem lorem pretium mi, vitae facilisis elit arcu ut ante. Nam consectetur quam eget erat pulvinar posuere. Aenean sed libero turpis. Nulla pellentesque imperdiet nulla id lacinia. Sed vel posuere risus. Etiam rhoncus dolor id congue molestie. Vestibulum ante ipsum primis in faucibus orci luctus et ultrices posuere cubilia curae; Sed ullamcorper hendrerit vestibulum. Suspendisse ac interdum ipsum. Integer risus erat, tempor ut ipsum sit amet, fermentum viverra lacus. Aliquam erat volutpat. Phasellus faucibus eu risus ut vulputate.</p>
      </div>

      <div class="about-author">
        <div class="author-photo" role="img" aria-label="Author photo placeholder"></div>
        <div class="author-bio">
          <h3>ABOUT THE AUTHOR</h3>
          <p>Nam tincidunt cursus diam et imperdiet. Vestibulum dignissim enim eu venenatis luctus. Nullam dignissim volutpat laoreet. Quisque vehicula eleifend hendrerit. Cras commodo facilisis mauris. Etiam eget libero blandit, scelerisque velit id, fermentum odio. Quisque pharetra porttitor sapien id aliquet. Proin sodales rhoncus elit.</p>
        </div>
      </div>
    </section>

    <section class="spine">
      <div class="spine-title">LANTERNS <span class="spine-amp">&amp;</span> LARKSPUR</div>
      <div class="spine-author">AUTHOR NAME</div>
    </section>

    <section class="front-cover">
      <h1 class="front-title">
        <span class="title-word">Lanterns</span>
        <span class="title-amp">&amp;</span>
        <span class="title-word">Larkspur</span>
      </h1>
      <div class="front-author">AUTHOR NAME</div>
    </section>
  </div>
</body>
</html>
```